Bluewater Getaways KT needs a new Website

We have an old website that is just that - old. We need a fresh website that is professional graphic designed that has the following features.
1. Can be updated by ourselves in some areas.
2. Has a shopping cart.
3. Has links to download PDF files
4. Has links to other pages in the website
5. Includes social media links
6. Has a client log-in area
Full details in brief provided.

SORRY BUT IT'S URGENT. We've taken too long to write the details and it is now urgent. So my apologies I will be asking for designers to work quickly.

We will continue to use our existing web hosting company and url. Their is a link to the old website in the Design Brief.
Updates

UPDATE:  Please see the new file UPDATE TO DESIGN BRIEF.
Thanks for all your submissions to date.  We hope the update will assist with your designs.
As indicated in previous messages, we are happy with the Home Page + 1 Page in order to select the designer to work with in creating the full design. 

Thankyou Designers.  Much appreciate your efforts.
It's getting late here on Norfolk so I won't have much chance too review any more designs this evening.
But for your information:
Designer 7318405 Ravindra Mehta is so far the closest to what we are seeking.
Thanks again. 

Reason: Have extended to Monday 7 October to give time for designers to submit after feedback today. Especially given the time differences

Target Market(s)

Very wide audience. Current client group not that tech savvy, but we hope to broaden our market and sell more creative products, and so website needs to consider how people now use media, ie tablets & iphones.

Industry/Entity Type

Shopping

Requirements
Nice to have
• PLEASE SEE THE "UPDATE TO THE DESIGN BRIEF"

```html
<!DOCTYPE html>
<html lang="en">
<head>
<meta charset="utf-8">
<title>Bluewater Getaways KT — Our Social Enterprise</title>
<link rel="stylesheet" href="https://fonts.googleapis.com/css2?family=Ubuntu:wght@400;500&family=Raleway:wght@400;500&family=Rokkitt:wght@300;400;600&display=swap">
<style>
:root{
  --orange:#f08a24;
  --orange-dark:#d86f12;
  --green:#2e9a3c;
  --ink:#222;
  --text:#555;
  --muted:#888;
  --rule:#d6d6d6;
  --dots:#cfcfcf;
  --link:#2b4a9c;
  --bg:#fff;
}
*{box-sizing:border-box;margin:0;padding:0}
html,body{width:1200px;height:694px;overflow:hidden;background:var(--bg)}
body{position:relative;font-family:"Ubuntu",sans-serif;color:var(--ink)}
.abs{position:absolute}

/* header */
.brand{left:150px;top:46px;display:flex;align-items:center;gap:12px}
.brand-dot{width:40px;height:40px;border-radius:50%;background:var(--orange)}
.brand-name{font-family:"Ubuntu",sans-serif;font-weight:500;font-size:21px;line-height:22px;color:var(--orange);width:150px}
.info h3{font-weight:400;font-size:11.5px;letter-spacing:.3px;margin-bottom:2px;color:var(--ink)}
.info p{font-size:9.5px;line-height:12.8px;color:#444;letter-spacing:.2px}
.location{left:720px;top:22px}
.contact{left:892px;top:22px}
.contact .row{display:flex}
.contact .row b{font-weight:500;width:68px}
.contact .email{margin-top:12px}
.contact a{color:var(--link);text-decoration:none}
.header-rule{left:150px;top:127px;width:900px;height:1px;background:var(--rule)}

/* columns */
.col-rule{width:1px;background:var(--rule);top:128px;height:531px}
.col-rule.left{left:331px}
.col-rule.right{left:853px}

.main-nav{left:150px;top:136px;width:172px;list-style:none}
.main-nav li{height:36.7px;display:flex;align-items:center;justify-content:space-between;font-size:10.5px;letter-spacing:.3px;border-bottom:1px dotted var(--dots);padding-left:2px}
.main-nav li:last-child{border-bottom:none}
.main-nav li.current{color:var(--orange)}
.main-nav .expand{font-size:9px;color:#999;margin-right:4px}

/* centre */
.title{left:354px;top:146px;width:477px;text-align:center}
.title h1{font-family:"Rokkitt",serif;font-weight:300;font-size:30px;color:var(--orange);letter-spacing:.5px;line-height:30px}
.title h2{font-family:"Rokkitt",serif;font-weight:400;font-size:17px;letter-spacing:1px;color:#333;margin-top:1px}
.values{left:354px;top:216px;width:477px;height:32px;border-top:1px solid var(--rule);display:flex;justify-content:space-around;align-items:center;font-family:"Raleway",sans-serif;font-size:13px;color:#333}
.values .sep{width:4px;height:4px;background:#ccc}
.hero{left:354px;top:248px;width:477px;height:210px;background:linear-gradient(160deg,#8a8371 0%,#b7ad90 45%,#a99f80 70%,#c9bfa0 100%)}
.hero-rule{left:354px;top:461px;width:477px;height:1px;background:var(--rule)}

.supported{left:354px;top:490px;width:114px;border-right:1px solid var(--rule);height:127px}
.supported h3{font-family:"Raleway",sans-serif;font-weight:400;font-size:16px;color:var(--orange);margin-bottom:5px}
.supported ul{list-style:none;font-family:"Raleway",sans-serif;font-size:11.5px;line-height:20.3px;color:#333}
.supported li::before{content:"• "}
.audience{left:482px;top:486px;width:355px}
.audience h2{font-family:"Rokkitt",serif;font-weight:300;font-size:24px;line-height:24px;color:#333}
.audience .rule{width:310px;height:1px;background:var(--rule);margin:11px 0 8px}
.audience p{font-family:"Raleway",sans-serif;font-size:14px;line-height:22px;color:var(--muted)}
.audience .sep{display:inline-block;width:4px;height:4px;background:#ccc;vertical-align:middle;margin:0 7px}

/* right column */
.media{left:866px;top:146px;width:168px;text-align:center}
.media h3{font-family:"Rokkitt",serif;font-weight:600;font-size:11.5px;letter-spacing:.3px}
.media-frame{margin:8px auto 0;width:168px;height:102px;background:linear-gradient(180deg,#3b4a3a 0%,#6d7a62 55%,#8a8a80 100%)}
.media p{font-family:Arial,sans-serif;font-size:10px;color:#333;margin-top:7px;line-height:14px}
.like{display:inline-block;border:1px solid #aab3c8;background:#eef0f5;font-size:9px;padding:0 5px;margin-right:6px}
.media a{color:var(--link);text-decoration:none}

.btn{left:866px;width:167px;height:28px;border-radius:2px;font-family:"Rokkitt",serif;font-weight:600;text-align:center;line-height:28px}
.btn.login{top:326px;background:linear-gradient(#fafafa,#e4e4e4);border:1px solid #c8c8c8;font-size:16px;color:#444}
.btn.festival{top:357px;background:linear-gradient(var(--orange),var(--orange-dark));color:#fff;font-size:12.5px;border:1px solid var(--orange-dark)}
.support{left:866px;top:396px;width:167px;height:137px;border-radius:2px;background:linear-gradient(180deg,#777 0%,#4a4a4a 60%,#2c2c2c 100%);overflow:hidden}
.support span{position:absolute;left:0;right:0;top:79px;height:32px;background:rgba(20,20,20,.6);color:var(--orange);font-family:"Rokkitt",serif;font-weight:600;font-size:22px;text-align:center;line-height:32px}

/* footer */
.footer-rule{left:150px;top:659px;width:900px;height:1px;background:var(--rule)}
.copyright{left:150px;top:669px;width:900px;text-align:center;font-family:Arial,sans-serif;font-size:9px;color:#222}
</style>
</head>
<body>

<div class="abs brand">
  <div class="brand-dot"></div>
  <div class="brand-name">Bluewater Getaways KT</div>
</div>

<div class="abs info location">
  <h3>LOCATION</h3>
  <p>Marsh Lane, Saltwood<br>PO Box 614<br>Kestrel Island NSW 2950<br>SOUTH PACIFIC<br>N.B.N. 417 552 108</p>
</div>

<div class="abs info contact">
  <h3>CONTACT</h3>
  <p class="row"><b>International:</b> + 67 31 58842</p>
  <p class="row"><b>Australia:</b>&nbsp;&nbsp;&nbsp;&nbsp;&nbsp;&nbsp;1800 463 218</p>
  <p class="row"><b>New Zealand:</b>&nbsp;&nbsp;0000 000 000</p>
  <p class="email"><b>Email:</b> hello@bluewatergetaways.org</p>
  <p><b>Friendhub:</b> <a href="#">bluewatergetaways</a></p>
</div>

<div class="abs header-rule"></div>
<div class="abs col-rule left"></div>
<div class="abs col-rule right"></div>

<ul class="abs main-nav">
  <li class="current">HOME</li>
  <li>OVERVIEW <span class="expand">[+]</span></li>
  <li>KESTREL ISLAND</li>
  <li>SERVICES <span class="expand">[+]</span></li>
  <li>OUR SHOP</li>
  <li>MAKE A BOOKING</li>
  <li>TESTIMONIALS</li>
</ul>

<div class="abs title">
  <h1>OUR SOCIAL ENTERPRISE</h1>
  <h2>ESTABLISHED JULY 2001</h2>
</div>

<div class="abs values">
  <span>DIVERSITY</span><i class="sep"></i><span>CARING</span><i class="sep"></i><span>COMMUNITY</span><i class="sep"></i><span>KESTREL ISLAND</span>
</div>

<div class="abs hero" role="img" aria-label="Coastal cliffs above a quiet bay on the island"></div>
<div class="abs hero-rule"></div>

<div class="abs supported">
  <h3>SUPPORTED</h3>
  <ul>
    <li>Holidays</li>
    <li>Travel</li>
    <li>Recreation</li>
    <li>Respite</li>
    <li>Creative projects</li>
  </ul>
</div>

<div class="abs audience">
  <h2>For people requiring support to participate in socially inclusive events.</h2>
  <div class="rule"></div>
  <p>Intellectual Disability<i class="sep"></i>Acquired Brain Injury Mental Health<i class="sep"></i>Sensory Impairment<i class="sep"></i>Frail Aged Mobility Challenged<i class="sep"></i>Siblings of children with Disabilities</p>
</div>

<div class="abs media">
  <h3>IMAGES &amp; VIDEO</h3>
  <div class="media-frame" role="img" aria-label="Video still of a horse-drawn carriage tour"></div>
  <p>to see more photographs and video's<br><span class="like">Like</span>our <a href="#">FRIENDHUB</a> page</p>
</div>

<div class="abs btn login">CLIENT LOGIN</div>
<div class="abs btn festival">OPEN LENS FILM FESTIVAL</div>
<div class="abs support" role="img" aria-label="Black and white photo of a community activity with a Support Us call to action"><span>SUPPORT US</span></div>

<div class="abs footer-rule"></div>
<p class="abs copyright">© Copyright Bluewater Getaways KT 2013. All Rights Reserved.</p>

</body>
</html>
```